New website for a commercial real estate consulting company

What we’re looking for in a new web site:
• Desktop and mobile friendly
• Clear navigation
• Strong graphics
• Professional appearance
• The ability to update it ourselves
• Site is for information purposes only – no transactions required
• Traffic counts – number of visits per page?
• A firm quote on costs to develop and launch
• SSL
Attached is a copy of the revised text we propose to use, including our new logo. (The pagination can be different than as shown.)
Our current website address is www.tamblinvaleadvisory.ca

```html
<!DOCTYPE html>
<html lang="en">
<head>
<meta charset="utf-8">
<title>For Lenders – Tamblin Vale Advisory</title>
<link href="https://fonts.googleapis.com/css2?family=Roboto:wght@400;500;700&display=swap" rel="stylesheet">
<style>
  :root {
    --brand: #2b3a8f;
    --brand-soft: #6a72b0;
    --ink: #1c1c1c;
    --rule: #e3e3e3;
    --menu-bg: #e6e8ee;
    --footer-bg: #f4f5f9;
    --footer-ink: #a2a4ad;
    --white: #ffffff;
  }
  * { box-sizing: border-box; margin: 0; padding: 0; }
  html, body { width: 1200px; height: 1200px; overflow: hidden; background: var(--white); }
  body { font-family: "Roboto", Arial, sans-serif; color: var(--ink); position: relative; }

  .topbar {
    position: absolute; left: 120px; top: 118px; width: 960px; height: 32px;
    background: var(--brand); color: var(--white); font-size: 15px; letter-spacing: 0.3px;
  }
  .topbar__item { position: absolute; top: 7px; display: flex; align-items: center; gap: 6px; }
  .topbar__phone { left: 15px; }
  .topbar__email { left: 310px; }
  .topbar__social { position: absolute; right: 16px; top: 9px; display: flex; gap: 18px; }
  .topbar__social span { width: 14px; height: 14px; border-radius: 50%; background: var(--white); display: block; }

  .header { position: absolute; left: 120px; top: 150px; width: 960px; height: 81px; border-bottom: 1px solid var(--rule); }
  .brand { position: absolute; left: 11px; top: 26px; display: flex; align-items: center; gap: 7px;
    color: var(--brand); font-size: 13px; font-weight: 500; }
  .brand__mark { width: 14px; height: 14px; background: var(--brand); }

  .nav { position: absolute; top: 0; left: 0; width: 100%; height: 100%; }
  .nav__link { position: absolute; top: 27px; font-size: 16px; color: var(--brand-soft); text-decoration: none; }
  .nav__link--active { color: var(--brand); }
  .nav__underline { position: absolute; left: 660px; top: 59px; width: 93px; height: 3px; background: var(--brand); }
  .nav__calendar { position: absolute; left: 905px; top: 24px; }

  .submenu { position: absolute; left: 780px; top: 232px; width: 123px; z-index: 3; list-style: none; }
  .submenu li { height: 35px; background: var(--menu-bg); color: var(--brand); font-size: 15.5px;
    padding-left: 18px; line-height: 35px; border-bottom: 1px solid var(--brand-soft); }
  .submenu li:last-child { border-bottom: none; }
  .submenu .is-current { background: var(--brand); color: var(--white); }

  .photo { position: absolute; left: 667px; top: 306px; width: 344px; height: 298px;
    background: linear-gradient(135deg, #4e6b73 0%, #8ea7a8 45%, #c9d6d2 70%, #7b8e92 100%);
    box-shadow: 0 2px 6px rgba(0,0,0,0.35); }

  .content { position: absolute; left: 187px; top: 291px; font-size: 13px; line-height: 19.2px; }
  .content h1 { font-size: 16px; font-weight: 400; color: var(--brand); margin-bottom: 31px; }
  .content p { margin-bottom: 19.2px; }
  .content .narrow { width: 410px; }
  .content .wide { width: 830px; }
  .content ul { list-style: none; margin-bottom: 19.2px; }
  .content li { position: relative; padding-left: 29px; }
  .content li::before { content: "•"; position: absolute; left: 0; font-size: 9px; }

  .footer { position: absolute; left: 120px; top: 970px; width: 960px; height: 112px; background: var(--footer-bg);
    text-align: center; font-size: 11px; color: var(--footer-ink); padding-top: 49px; letter-spacing: 0.2px; }
</style>
</head>
<body>
  <div class="topbar">
    <div class="topbar__item topbar__phone">
      <svg width="12" height="12" viewBox="0 0 24 24"><path fill="#fff" d="M6.6 10.8a15 15 0 0 0 6.6 6.6l2.2-2.2c.3-.3.7-.4 1-.2 1.1.4 2.3.6 3.6.6.6 0 1 .4 1 1V20c0 .6-.4 1-1 1A17 17 0 0 1 3 4c0-.6.4-1 1-1h3.5c.6 0 1 .4 1 1 0 1.3.2 2.5.6 3.6.1.3 0 .7-.2 1z"/></svg>
      905-555-0148
    </div>
    <div class="topbar__item topbar__email">
      <svg width="15" height="12" viewBox="0 0 20 16"><rect width="20" height="16" rx="2" fill="#fff"/><path d="M1 2l9 7 9-7" stroke="#2b3a8f" stroke-width="2" fill="none"/></svg>
      mara.ellison@tamblinvaleadvisory.com
    </div>
    <div class="topbar__social" aria-label="Social links"><span></span><span></span><span></span></div>
  </div>

  <header class="header">
    <div class="brand"><span class="brand__mark"></span>Tamblin Vale Advisory</div>
    <nav class="nav">
      <a class="nav__link" style="left:416px">Home</a>
      <a class="nav__link" style="left:519px">Who We Are</a>
      <a class="nav__link nav__link--active" style="left:663px">What We Do</a>
      <a class="nav__link" style="left:804px">Contact</a>
      <span class="nav__underline"></span>
      <svg class="nav__calendar" width="32" height="31" viewBox="0 0 32 31" aria-label="Calendar">
        <rect x="1" y="4" width="27" height="26" fill="none" stroke="#2b3a8f" stroke-width="1.5"/>
        <line x1="1" y1="9" x2="28" y2="9" stroke="#2b3a8f" stroke-width="1.5"/>
        <g fill="#2b3a8f">
          <rect x="5" y="1" width="2" height="5"/><rect x="11" y="1" width="2" height="5"/><rect x="17" y="1" width="2" height="5"/><rect x="23" y="1" width="2" height="5"/>
          <rect x="5" y="12" width="3" height="3"/><rect x="10" y="12" width="3" height="3"/><rect x="15" y="12" width="3" height="3"/><rect x="20" y="12" width="3" height="3"/>
          <rect x="5" y="17" width="3" height="3"/><rect x="10" y="17" width="3" height="3"/><rect x="15" y="17" width="3" height="3"/><rect x="20" y="17" width="3" height="3"/>
          <rect x="5" y="22" width="3" height="3"/><rect x="10" y="22" width="3" height="3"/><rect x="15" y="22" width="3" height="3"/><rect x="20" y="22" width="3" height="3"/>
        </g>
        <path d="M28 12 L31 30 L28 30" fill="none" stroke="#2b3a8f" stroke-width="1.2"/>
      </svg>
    </nav>
  </header>

  <ul class="submenu">
    <li>For Owners</li>
    <li>For Buyers</li>
    <li class="is-current">For Lenders</li>
    <li>For Brokers</li>
  </ul>

  <div class="photo" role="img" aria-label="Photo of colleagues at laptops reviewing paperwork with a pen"></div>

  <main class="content">
    <h1>For Lenders</h1>
    <p class="narrow">Today’s real estate lenders are squeezed between the triple pressures of aggressive lending targets, staff budget constraints and ever-tightening regulation.&nbsp; Everyone is being asked to <strong>“do more, with less”</strong>.&nbsp; We can help, cost-effectively.</p>
    <p class="narrow"><strong>On the new business side, we have helped clients with:</strong></p>
    <ul>
      <li>Staff training;</li>
      <li>Underwriting;</li>
      <li>Lease summaries;</li>
      <li>Credit adjudication.</li>
    </ul>
    <p class="narrow"><strong>On the portfolio administration side, we have helped clients with:</strong></p>
    <ul>
      <li>Defaulted loan management;</li>
      <li>Portfolio risk assessments</li>
      <li>Annual reviews;</li>
      <li>Procedural audits</li>
    </ul>
    <p class="wide">Our team has a combined total of more than 50 years’ experience in all facets of real estate lending.&nbsp;&nbsp; We have hands-on experience in the design and creation of institutional mortgage and default management departments, including all staffing and systems needs, strategic and tactical goals, policies and procedures, and internal risk rating systems.</p>
    <p class="wide">One of the most popular services we provide our lender clients is the preparation of concise and accurate lease summaries and estoppel reviews.&nbsp;&nbsp; With decades of hands-on experience, we have reviewed literally thousands of commercial leases.</p>
    <p class="wide">We present our lease and estoppel reviews in whatever format the client requires, ranging from a multi-page narrative précis of each lease to a highly condensed spreadsheet summary report.&nbsp; We are happy to work with your underwriters to design a format that completely meets your needs.</p>
  </main>

  <footer class="footer">Copyright © Tamblin Vale Advisory. All rights reserved.</footer>
</body>
</html>
```